Wedding Startup Full Website Design

We've just completed our online platform and need to create a website that represents our brand and vision, and clearly communicates our features and value proposition to potential users. There are a minimum of 4 pages that need to be designed. One geared toward wedding professionals (venues/vendors/coordinators), another toward engaged couples, one showcasing features, and an 'About Us' page.

The designer will creative freedom to create a unique UI/UX as long as it represents our brand and is relevant to our target audience/market. The ideal candidate will be able to assume the mindset of someone working in the wedding industry and/or an engaged couple. Ability to create illustrations is a plus.

Copy will be provided as needed. We will reimburse for stock images (pending approval before purchasing), but sourcing the stock images will be the responsibility of the designer.

Our current website: https://www.trelmora.com
Updates

Our project has now been guaranteed! We look forward to finding the perfect design for our site pages!

Still waiting for a design that stands out from the rest and aligns with the creative brief.

Target Market(s)

Wedding Professionals and Engaged Couples

Industry/Entity Type

Wedding

Number of Pages Required

4 page

Font styles to use
Sans Serif

Colors
ffffff
fbd4d5
f59195
33a6d7
cadf82
86cfc6

Requirements
Must have
• Common sense stuff like having a unified brand that accurately represents our platform, speaks to our target market, and clearly articulates our vision
Nice to have
• Illustrations
Should not have
• Overly cheesy or childish. We want to be professional but still embrace the wedding culture.

```html
<!DOCTYPE html>
<html lang="en">
<head>
<meta charset="utf-8">
<title>Trelmora — Smarter Wed Planning</title>
<link href="https://fonts.googleapis.com/css2?family=Merriweather:wght@300;400&family=Open+Sans:wght@400;600&display=swap" rel="stylesheet">
<style>
:root{
  --white:#ffffff;
  --blush:#fbd4d5;
  --coral:#f59195;
  --sky:#33a6d7;
  --sky-soft:#5aa9de;
  --ink:#3b3b3b;
  --mist:#ebebe7;
  --serif:"Merriweather", Georgia, serif;
  --sans:"Open Sans", Arial, sans-serif;
}
*{box-sizing:border-box;margin:0;padding:0}
html,body{width:1200px;height:3197px;overflow:hidden;background:var(--white)}
body{font-family:var(--sans);color:var(--ink)}
.page{position:relative;width:1200px;height:3197px;overflow:hidden;background:var(--mist)}
.abs{position:absolute}

/* hero */
.hero-photo{position:absolute;left:0;top:0;width:1200px;height:830px;
  background:
    radial-gradient(ellipse 260px 330px at 150px 120px,rgba(238,232,220,.95) 0%,rgba(225,218,203,.7) 40%,rgba(225,218,203,0) 75%),
    radial-gradient(ellipse 220px 260px at 380px 260px,rgba(48,46,50,.85) 0%,rgba(48,46,50,0) 75%),
    radial-gradient(ellipse 420px 160px at 620px 230px,rgba(150,128,96,.75) 0%,rgba(150,128,96,0) 75%),
    radial-gradient(ellipse 340px 260px at 1020px 160px,rgba(118,142,88,.9) 0%,rgba(118,142,88,0) 75%),
    radial-gradient(ellipse 520px 260px at 900px 540px,rgba(60,78,40,.9) 0%,rgba(60,78,40,0) 75%),
    radial-gradient(ellipse 500px 240px at 260px 560px,rgba(86,104,56,.9) 0%,rgba(86,104,56,0) 75%),
    linear-gradient(180deg,#8f9a72 0%,#66773f 28%,#52642f 55%,#7e8c55 78%,#c9cbbd 100%)}
.hero-curve{position:absolute;left:0;top:640px}
.nav{position:absolute;left:160px;top:51px;width:880px;height:52px;background:var(--white);border-radius:26px;
  box-shadow:0 2px 8px rgba(0,0,0,.15)}
.nav a{position:absolute;top:18px;font-size:12px;color:var(--ink);text-decoration:none;letter-spacing:.3px}
.nav-logo{position:absolute;left:534px;top:30px;width:132px;height:80px;border-radius:40px;background:var(--white);
  display:flex;align-items:center;justify-content:center;font-family:var(--sans);font-weight:600;font-size:28px;color:var(--sky)}
.social{position:absolute;top:13px;width:27px;height:27px;border-radius:50%;background:#cfcfcf}
.demo-btn{position:absolute;left:718px;top:9px;width:146px;height:34px;border-radius:17px;background:var(--coral);
  color:var(--white);font-size:11px;font-weight:600;text-align:center;line-height:34px;letter-spacing:.5px}
.hero-box{position:absolute;left:270px;top:288px;width:661px;height:245px;background:rgba(40,40,40,.45);
  border:3px solid rgba(60,60,60,.7)}
.hero-box::after{content:"";position:absolute;left:-18px;top:-18px;right:18px;bottom:18px;border:3px solid rgba(70,70,70,.55)}
.hero-title{position:absolute;left:0;width:100%;top:58px;text-align:center;font-family:var(--serif);font-weight:300;
  font-size:38px;color:var(--white);letter-spacing:1px}
.tag{background:var(--sky-soft);color:var(--white);padding:0 12px}
.hero-sub{position:absolute;left:0;width:100%;top:112px;text-align:center;font-size:21px;color:var(--white)}
.btn{position:absolute;height:36px;border-radius:18px;background:var(--coral);color:var(--white);font-size:11px;
  font-weight:600;text-align:center;line-height:36px;letter-spacing:.6px}

/* steps */
.steps-bg{position:absolute;left:0;top:700px;width:1200px;height:666px;
  background:
    radial-gradient(ellipse 300px 420px at 740px 330px,rgba(170,160,150,.45) 0%,rgba(170,160,150,0) 75%),
    radial-gradient(ellipse 260px 360px at 380px 420px,rgba(200,195,188,.55) 0%,rgba(200,195,188,0) 75%),
    radial-gradient(ellipse 400px 200px at 1000px 560px,rgba(150,158,128,.35) 0%,rgba(150,158,128,0) 75%),
    linear-gradient(180deg,#ebebe7 0%,#e6e6e1 50%,#d9dad2 100%)}
.section-title{position:absolute;left:0;width:1200px;text-align:center;font-family:var(--serif);font-weight:300;
  font-size:40px;color:var(--coral)}
.step{position:absolute;width:222px;height:222px;border-radius:50%;background:var(--white);
  border:10px solid #56624a;text-align:center;padding:48px 30px 0}
.step h3{font-family:var(--serif);font-weight:300;font-size:24px;color:var(--coral);margin-bottom:14px}
.step p{font-size:12px;line-height:17px;color:var(--ink)}
.step .link{color:var(--sky);display:block}

/* feature strip */
.feature{position:absolute;top:1366px;width:400px;height:222px;overflow:hidden;padding:38px 28px}
.feature h3{font-family:var(--serif);font-weight:300;font-size:24px;line-height:28px;color:var(--coral);margin-bottom:18px}
.feature p{font-size:12px;line-height:17px;color:#e6e6e6;width:250px}
.feature .badge{position:absolute;right:-10px;bottom:-20px;width:110px;height:110px;border-radius:50%;
  display:flex;align-items:center;justify-content:center;padding:0 14px 18px 0}

/* why cards */
.card{position:absolute;overflow:hidden;text-align:center;color:var(--white);padding:0 20px}
.card svg{display:block;margin:0 auto}
.card h4{font-family:var(--serif);font-weight:300;font-size:20px;margin:14px 0 10px}
.card p{font-size:12px;line-height:17px;color:#e4e4e4}

/* get started today */
.cta-bg{position:absolute;left:0;top:2333px;width:1200px;height:600px;
  background:
    radial-gradient(ellipse 260px 300px at 80px 200px,rgba(210,208,204,.7) 0%,rgba(210,208,204,0) 75%),
    radial-gradient(ellipse 260px 300px at 1120px 260px,rgba(215,212,208,.6) 0%,rgba(215,212,208,0) 75%),
    linear-gradient(180deg,#ffffff 0%,#f4f4f3 60%,#ececea 100%)}
.bride-photo{position:absolute;left:340px;top:2343px;width:520px;height:520px;
  background:
    radial-gradient(ellipse 70px 90px at 268px 100px,#c98f78 0%,#d6a894 55%,rgba(214,168,148,0) 100%),
    radial-gradient(ellipse 90px 60px at 250px 40px,#6d4a38 0%,rgba(109,74,56,0) 100%),
    radial-gradient(ellipse 60px 40px at 160px 150px,rgba(150,104,60,.8) 0%,rgba(150,104,60,0) 100%),
    radial-gradient(ellipse 70px 60px at 430px 490px,rgba(200,168,60,.85) 0%,rgba(200,168,60,0) 100%),
    radial-gradient(ellipse 60px 40px at 270px 450px,rgba(180,140,110,.8) 0%,rgba(180,140,110,0) 100%),
    radial-gradient(ellipse 230px 260px at 260px 240px,rgba(232,228,226,.95) 0%,rgba(240,238,236,.6) 60%,rgba(240,238,236,0) 100%)}
.cta-band{position:absolute;left:0;top:2525px;width:1200px;height:224px;background:rgba(255,255,255,.82)}
.cta-text{position:absolute;left:270px;top:2627px;width:660px;text-align:center;font-size:12px;line-height:18px;color:var(--ink)}

/* footer */
.footer-photo{position:absolute;left:0;top:2877px;width:1200px;height:292px;
  background:
    radial-gradient(ellipse 220px 200px at 930px 200px,rgba(140,110,96,.8) 0%,rgba(140,110,96,0) 75%),
    radial-gradient(ellipse 160px 160px at 1060px 150px,rgba(90,80,72,.9) 0%,rgba(90,80,72,0) 75%),
    linear-gradient(90deg,#3b3c3a 0%,#4a4b47 45%,#5d5550 75%,#4a4540 100%)}
.footer-logo{position:absolute;left:0;width:1200px;top:3036px;text-align:center;font-weight:600;font-size:36px;color:var(--sky)}
.footer-nav{position:absolute;left:0;width:1200px;top:3102px;text-align:center;font-size:14px;color:var(--white)}
.footer-nav span{margin:0 22px}
.footer-nav i{font-style:normal;color:var(--sky)}
.legal{position:absolute;left:0;top:3169px;width:1200px;height:28px;background:var(--coral);color:var(--white);
  text-align:center;font-size:11px;line-height:28px}
</style>
</head>
<body>
<div class="page">

  <!-- hero -->
  <div class="steps-bg" role="img" aria-label="Faded wedding couple photograph behind the steps"></div>
  <div class="hero-photo" role="img" aria-label="Bride and groom seated on a wooden footbridge among tall summer grasses"></div>
  <svg class="hero-curve" width="1200" height="200" viewBox="0 0 1200 200" aria-hidden="true">
    <path d="M0 40 Q440 60 570 140 L600 172 L630 140 Q760 60 1200 40 V200 H0Z" fill="#ebebe7"/>
    <path d="M0 40 Q440 60 570 140 L600 172 L630 140 Q760 60 1200 40" fill="none" stroke="#fff" stroke-width="2"/>
  </svg>

  <header class="nav">
    <a style="left:58px">ABOUT US</a>
    <a style="left:163px">FEATURES</a>
    <a style="left:265px">FOR COUPLES</a>
    <span class="social" style="left:598px"></span>
    <span class="social" style="left:631px"></span>
    <span class="social" style="left:664px"></span>
    <span class="demo-btn">ACESS DEMO</span>
  </header>
  <div class="nav-logo">Trelmora</div>

  <section class="hero-box">
    <h1 class="hero-title">WELCOME TO <span class="tag">TRELMORA</span></h1>
    <p class="hero-sub">Smarter Wed Planning™</p>
    <span class="btn" style="left:258px;top:182px;width:145px">GET STARTED</span>
  </section>

  <!-- how to get started -->
  <h2 class="section-title" style="top:860px">HOW TO <span class="tag">GET STARTED</span></h2>

  <div class="step" style="left:204px;top:1086px;border-color:#3f4c5a">
    <h3>Sign Up</h3>
    <p>Create a free account on Trelmora to access popular collaboration tools.<span class="link">Get Started</span></p>
  </div>
  <div class="step" style="left:488px;top:954px;border-color:#9a8a4a">
    <h3>Collaborate</h3>
    <p>Add clients within the application to better organize and manage event details.</p>
  </div>
  <div class="step" style="left:771px;top:1076px;border-color:#5f7a3c">
    <h3>Connect</h3>
    <p>Linking your bank account within Trelmora to allow for seamless payments and monitoring.</p>
  </div>

  <!-- feature strip -->
  <div class="feature" style="left:0;background:radial-gradient(ellipse 120px 160px at 330px 80px,#6a625c,rgba(106,98,92,0)),linear-gradient(90deg,#3c3c3e,#55524f)" role="img" aria-label="Guests at an evening reception">
    <h3>Realtime<br>Collaboration.</h3>
    <p>There are often disconnects in the communication channel. At the core of Trelmora we ensure everyone is updated in real time with event information.</p>
    <span class="badge" style="background:var(--sky-soft)">
      <svg width="46" height="46" viewBox="0 0 46 46" fill="none" stroke="#f59195" stroke-width="2.5"><path d="M23 6C13 6 5 12.5 5 21c0 4 2 7.5 5 10l-2 8 9-4c2 .6 4 1 6 1 10 0 18-6.5 18-15S33 6 23 6Z"/><path d="M15 19h16M15 25h11"/></svg>
    </span>
  </div>
  <div class="feature" style="left:400px;background:radial-gradient(ellipse 120px 180px at 200px 120px,rgba(180,200,220,.8),rgba(180,200,220,0)),linear-gradient(135deg,#4b8fc4,#7fb3d9 60%,#9cc4de)" role="img" aria-label="Couple in silhouette under a blue sky">
    <h3 style="color:var(--white)">Cloud<br>Storage</h3>
    <p style="color:#eef5fb">No longer do you have to remember where every piece of information is saved. With Trelmora all your information is available in one central location.</p>
    <span class="badge" style="background:var(--coral)">
      <svg width="48" height="40" viewBox="0 0 48 40" fill="none" stroke="#fff" stroke-width="2.5"><path d="M13 32H10a8 8 0 0 1 0-16 12 12 0 0 1 23-3 9 9 0 0 1 6 19h-4"/><path d="M24 36V20M18 26l6-6 6 6"/></svg>
    </span>
  </div>
  <div class="feature" style="left:800px;background:radial-gradient(ellipse 160px 120px at 300px 80px,#7a706a,rgba(122,112,106,0)),linear-gradient(90deg,#4a4744,#5f5a55)" role="img" aria-label="Wedding guests seated at a ceremony">
    <h3>Notifications<br>&amp; Deadlines</h3>
    <p>Every detail is important and matters. Trelmora helps make sure that all the information for an event are inputted and updated in a timely manner.</p>
    <span class="badge" style="background:var(--sky-soft)">
      <svg width="42" height="46" viewBox="0 0 42 46" fill="none" stroke="#f59195" stroke-width="2.5"><path d="M21 5c-7 0-12 5-12 12v10l-5 7h34l-5-7V17c0-7-5-12-12-12Z"/><path d="M16 38a5 5 0 0 0 10 0"/></svg>
    </span>
  </div>

  <!-- why -->
  <div class="abs" style="left:0;top:1588px;width:1200px;height:745px;background:var(--white)"></div>
  <h2 class="section-title" style="top:1638px">Why <span class="tag">Trelmora</span></h2>

  <div class="card" style="left:162px;top:1711px;width:277px;height:284px;background:linear-gradient(180deg,#1f2a3c,#3a4150 60%,#6b5a48)" role="img" aria-label="Couple silhouetted at dusk">
    <svg style="margin-top:62px" width="56" height="56" viewBox="0 0 56 56" fill="none" stroke="#fff" stroke-width="2"><circle cx="28" cy="31" r="18"/><path d="M28 31V20M28 31l8 5M24 8h8M28 8v5"/></svg>
    <h4>Saves Everyone Time</h4>
    <p>Trelmora streamlines certain processes allowing you to spend more time on the things your want to or just relax!</p>
  </div>
  <div class="card" style="left:462px;top:1711px;width:277px;height:284px;background:linear-gradient(135deg,#5a4a44,#7d6a60 50%,#4d4340)" role="img" aria-label="Wall of printed review photographs">
    <svg style="margin-top:62px" width="60" height="56" viewBox="0 0 60 56" fill="none" stroke="#fff" stroke-width="2"><path d="M6 8h30v20H18l-8 7v-7H6Z"/><path d="M40 20h14v20h-4v7l-8-7H24v-8"/></svg>
    <h4>Better Client Reviews</h4>
    <p>With Trelmora you can offer your clients an experience they will rave about, leading to better reviews and more clients.</p>
  </div>
  <div class="card" style="left:763px;top:1711px;width:277px;height:284px;background:linear-gradient(135deg,#3d3d3d,#5d5d5d 55%,#2e2e2e)" role="img" aria-label="Laptop and phone on a desk">
    <svg style="margin-top:62px" width="64" height="56" viewBox="0 0 64 56" fill="none" stroke="#fff" stroke-width="2"><rect x="10" y="8" width="44" height="28" rx="2"/><path d="M4 42h40"/><rect x="46" y="24" width="14" height="24" rx="2"/></svg>
    <h4>Accessible on Any Device</h4>
    <p>Flexibility is key, which is why Trelmora's platform was built to be accessed on your phone, tablet or desktop.</p>
  </div>
  <div class="card" style="left:162px;top:2018px;width:426px;height:277px;background:linear-gradient(135deg,#4a4b4d,#6e6d6a 50%,#3a3b3d)" role="img" aria-label="Two people shaking hands">
    <svg style="margin-top:70px" width="52" height="52" viewBox="0 0 52 52" fill="none" stroke="#fff" stroke-width="2"><rect x="6" y="10" width="40" height="36" rx="2"/><path d="M6 20h40M16 5v10M36 5v10M14 28h4M24 28h4M34 28h4M14 36h4M24 36h4"/></svg>
    <h4>Simplified Organization</h4>
    <p>Trelmora was built with organization in mind. All event details are in one place making executing an event easier.</p>
  </div>
  <div class="card" style="left:612px;top:2018px;width:426px;height:277px;background:linear-gradient(135deg,#3a3a3a,#5b5a57 55%,#2f2f2f)" role="img" aria-label="Stack of coins">
    <svg style="margin-top:64px" width="48" height="56" viewBox="0 0 48 56" fill="none" stroke="#fff" stroke-width="2"><path d="M16 6h16l-5 10h-6Z"/><path d="M21 16C10 22 5 32 5 40c0 8 7 11 19 11s19-3 19-11c0-8-5-18-16-24"/><path d="M29 29c-1-2-3-3-5-3-3 0-5 1.5-5 4s2 3.5 5 4 5 1.5 5 4-2 4-5 4-4-1-5-3M24 23v3M24 42v3"/></svg>
    <h4>Lower Transaction Fees</h4>
    <p>We offer the lowest online processing fees (2.65%) in the wedding industry, meaning you keep more of your money.</p>
  </div>

  <!-- get started today -->
  <div class="cta-bg" role="img" aria-label="Soft white veil texture background"></div>
  <div class="bride-photo" role="img" aria-label="Bride in a veil holding autumn leaves"></div>
  <div class="cta-band"></div>
  <h2 class="section-title" style="top:2562px"><span class="tag">Get Started</span> Today</h2>
  <p class="cta-text">We recently launched a demo version of Trelmora to allow users to see and interact with our platform. Create a free account and see how Trelmora is changing the wedding planning process!</p>
  <span class="btn" style="left:528px;top:2675px;width:145px">GET STARTED</span>

  <!-- footer -->
  <footer>
    <div class="footer-photo" role="img" aria-label="Couple embracing in soft evening light"></div>
    <svg class="abs" style="left:0;top:2876px" width="1200" height="110" viewBox="0 0 1200 110" aria-hidden="true">
      <path d="M0 0H1200V14Q770 28 632 72L600 96L568 72Q430 28 0 14Z" fill="#ececea"/>
    </svg>
    <div class="footer-logo">Trelmora</div>
    <nav class="footer-nav"><span>About Us</span><i>•</i><span>Features</span><i>•</i><span>For Couples</span></nav>
    <div class="legal">© 2018 trelmora. All Rights Reserved.</div>
  </footer>
</div>
</body>
</html>
```